Webdesign für Rheinau Vita Forschungsbund e.V.
Zielgruppe
Vereinsmitglieder aus der Bio-Tech-Branche, Öffentlichkeit
Aufgabenstellung
Wir benötigen ein Webdesign für die Website des Rheinau Vita Forschungsbund e.V., zu liefern als PSD-Datei.

```html
<!DOCTYPE html>
<html lang="de">
<head>
<meta charset="utf-8">
<title>Rheinau Vita Forschungsbund e.V. – Über uns</title>
<link href="https://fonts.googleapis.com/css2?family=Arimo:ital,wght@0,400;0,700;1,700&display=swap" rel="stylesheet">
<style>
:root{
  --teal:#4a9fb0;
  --link:#3a9cb6;
  --text:#333;
  --muted:#888;
  --line:#d6d6d6;
  --header-bg:#f7f7f7;
  --band-bg:#efefef;
  --footer-bg:#f2f2f2;
}
*{margin:0;padding:0;box-sizing:border-box}
html,body{width:1200px;height:778px;overflow:hidden;background:#fff}
body{font-family:'Arimo',Arial,sans-serif;color:var(--text);position:relative}
.page{position:absolute;left:119px;top:0;width:962px;height:778px;border-left:1px solid #c8c8c8;border-right:1px solid #c8c8c8}
.topbar{position:absolute;left:0;top:0;width:100%;height:7px;background:var(--teal)}
.header{position:absolute;left:0;top:7px;width:100%;height:148px;background:var(--header-bg);border-bottom:1px solid #c4c4c4}
.brand{position:absolute;left:34px;top:96px;display:flex;align-items:center;gap:10px;font-size:19px;font-weight:700;letter-spacing:1px;color:#2b2b2b}
.brand-dot{width:14px;height:14px;border-radius:50%;background:var(--teal)}
.contact{position:absolute;left:768px;top:12px;font-size:12px;line-height:18.2px;color:#333}
.contact a{color:var(--link);text-decoration:none}
.langbar{position:absolute;left:0;top:155px;width:100%;height:26px;background:linear-gradient(#f8f8f8,#ececec);border-bottom:1px solid #c8c8c8}
.flags{position:absolute;left:816px;top:5px;display:flex;gap:8px}
.flags svg{display:block}
.nav{position:absolute;left:0;top:181px;width:199px;height:530px;border-right:1px solid #e2e2e2}
.nav ul{list-style:none;margin-top:22px}
.nav li{height:23px;border-top:1px solid #e4e4e4;font-size:14px;line-height:22px;padding-left:27px;color:#333}
.nav li:last-child{border-bottom:1px solid #e4e4e4}
.nav li.active{border-left:4px solid var(--teal);padding-left:23px;position:relative}
.nav li.active::after{content:"";position:absolute;right:0;top:0;width:4px;height:22px;background:var(--teal)}
.nav li.sub{padding-left:44px}
.nav li.sub::before{content:"└";color:var(--teal);font-size:11px;margin-right:8px}
.content{position:absolute;left:222px;top:204px;width:515px;font-size:14px;line-height:23px;color:#333}
.content strong{font-weight:700}
.content a{color:var(--link);text-decoration:none}
.content p{margin-bottom:23px}
.highlight{position:relative;height:82px;margin:8px 0 0}
.network-img{position:absolute;left:42px;top:0;width:92px;height:66px;border-radius:6px;background:radial-gradient(circle at 50% 50%,#d9d9d9,#f4f4f4 70%)}
.highlight em{position:absolute;left:180px;top:6px;font-weight:700;font-style:italic;color:#777;font-size:14px;line-height:23px}
.lab-img{position:absolute;left:606px;top:618px;width:100px;height:67px;border-radius:4px;background:linear-gradient(135deg,#eef3f6,#c9dde6 60%,#f4f4f4)}
.lab-caption{position:absolute;left:496px;top:674px;font-size:10px;color:var(--link)}
.sidebar{position:absolute;left:748px;top:181px;width:213px;height:530px;border-left:1px solid #e2e2e2}
.sidebar h2{position:absolute;left:19px;top:26px;font-size:14px;font-weight:700;color:#333}
.events{position:absolute;left:19px;top:57px;list-style:none;font-size:12px;line-height:14px;color:#333;width:180px}
.events li{margin-bottom:15.5px}
.feature-title{position:absolute;left:21px;top:358px;width:180px;font-size:12px;font-weight:700;line-height:14px;color:var(--link)}
.feature-img{position:absolute;left:19px;top:394px;width:173px;height:117px;background:linear-gradient(135deg,#6f8f9a,#b8c9cf 50%,#9fb3b9)}
.footer{position:absolute;left:0;top:711px;width:100%;height:67px;background:var(--footer-bg);border-top:1px solid #c4c4c4}
.copyright{position:absolute;left:18px;top:29px;font-size:12px;color:#888}
.partner{position:absolute;background:#d9d9d9}
.p1{left:327px;top:16px;width:38px;height:38px}
.p2{left:421px;top:28px;width:123px;height:22px;background:#dcdcdc}
.p3{left:586px;top:11px;width:76px;height:43px;border-radius:4px;background:#e2e2e2}
</style>
</head>
<body>
<div class="page">
  <div class="topbar"></div>
  <header class="header">
    <div class="brand"><span class="brand-dot"></span>RHEINAU VITA FORSCHUNGSBUND</div>
    <address class="contact" style="font-style:normal">
      Rheinau Vita Forschungsbund e.V.<br>
      Lindenhainweg 12<br>
      60599 Rheinau<br>
      Telefon +49 00 | 123 456 10<br>
      Telefax +49 00 | 123 456 46<br>
      E-Mail: <a href="#">info@rheinau-vita.de</a><br>
      Web: <a href="#">www.rheinau-vita.de</a>
    </address>
  </header>
  <div class="langbar">
    <div class="flags">
      <svg width="19" height="13" aria-label="Deutsch"><rect width="19" height="4.4" fill="#222"/><rect y="4.3" width="19" height="4.4" fill="#d00"/><rect y="8.6" width="19" height="4.4" fill="#fc0"/></svg>
      <svg width="19" height="13" aria-label="English"><rect width="19" height="13" fill="#eee"/><g fill="#b22"><rect width="19" height="1.3"/><rect y="2.6" width="19" height="1.3"/><rect y="5.2" width="19" height="1.3"/><rect y="7.8" width="19" height="1.3"/><rect y="10.4" width="19" height="1.3"/></g><rect width="8" height="6.5" fill="#33a"/></svg>
      <svg width="19" height="13" aria-label="Français"><rect width="6.4" height="13" fill="#1a3fa0"/><rect x="6.3" width="6.4" height="13" fill="#fff"/><rect x="12.6" width="6.4" height="13" fill="#e22"/></svg>
    </div>
  </div>
  <nav class="nav">
    <ul>
      <li>Startseite</li>
      <li class="active">Über uns</li>
      <li>Struktur</li>
      <li>Ansprechpartner</li>
      <li>Mitglieder</li>
      <li>Region</li>
      <li>Allgemeines</li>
      <li class="sub">Infrastruktur</li>
      <li class="sub">Internationalität</li>
      <li>Service</li>
      <li>Jobbörse</li>
      <li>Linkliste</li>
      <li>Downloads</li>
      <li>Kontakt</li>
      <li>ABG</li>
      <li>Impressum</li>
      <li>Sitemap</li>
    </ul>
  </nav>
  <main class="content">
    <p><strong>Der Rheinau Vita Forschungsbund</strong> versteht sich als Schrittmacher für die Biotechnologie-Region Rhein-Main. Wir sind qualifizierter Ansprechpartner für Unternehmen, Politik und Medien und Interessen-vertretung für alle, die in der Wertschöpfungskette von der Grundlagenforschung bis zum fertigen Produkt und seiner Vermarktung arbeiten.</p>
    <div class="highlight">
      <div class="network-img" role="img" aria-label="Netzwerk aus verbundenen Metallkugeln mit roter Kugel in der Mitte"></div>
      <em>Hierfür bieten wir ein in der Region<br>ein einzigartiges Netzwerk.</em>
    </div>
    <p>Auch Deutschland bleibt nicht verschont: Kürzlich gab es einen spektakulären Fall von Medikamentenfälschung in Dillingen, Bayern. Dort wurden Fälschungen von CAPILLON® 1 mg <a href="#">Filmtabletten (Finasterid)</a> sichergestellt, einem Medikament zur Behandlung des erblich beding- ten Haarausfalls bei Männern. Inzwischen ist der Fall abgeschlossen.</p>
    <p>Gegen den Drahtzieher eines offensichtlich international agierenden Rings von Medikamentenfälschern wurde Strafbefehl erlassen.</p>
  </main>
  <div class="lab-img" role="img" aria-label="Laborglaswaren mit bunten Reagenzgläsern"></div>
  <div class="lab-caption">Rheinau Vita Forschungsbund</div>
  <aside class="sidebar">
    <h2>Veranstaltungen</h2>
    <ul class="events">
      <li>07.12.10 Veranstaltung Nummer 1 zum Thema x</li>
      <li>10.12.10 Veranstaltung Nummer 2 zum Thema y</li>
      <li>24.12.10 Veranstaltung Nummer 3 zum Thema z</li>
      <li>07.01.11 Veranstaltung Nummer 1 zum Thema x</li>
      <li>10.01.11 Veranstaltung Nummer 2 zum Thema y</li>
      <li>24.01.11 Veranstaltung Nummer 3 zum Thema z</li>
    </ul>
    <div class="feature-title">Arzneimittelfälschungen - ein unterschätztes Problem</div>
    <div class="feature-img" role="img" aria-label="Forschende im Labor mit Schutzbrillen und Glaskolben"></div>
  </aside>
  <footer class="footer">
    <div class="copyright">© 2011 - RVF</div>
    <div class="partner p1"></div>
    <div class="partner p2"></div>
    <div class="partner p3"></div>
  </footer>
</div>
</body>
</html>
```